Game Design from Mock ups

Looking for a simple design based on the images attached.

Should be a simple color scheme, not the same colored posted in the images. Flat design would be best.

Both pages should be designed (Menu and Gameplay)

```html
<!DOCTYPE html>
<html lang="en">
<head>
<meta charset="utf-8">
<title>Emoji Puzzles – Menu and Gameplay</title>
<link rel="stylesheet" href="https://fonts.googleapis.com/css2?family=Arimo:wght@400;700&display=swap">
<style>
:root{
  --menu-frame:#263238;
  --game-frame:#37474f;
  --brand-teal:#16697a;
  --paper:#fdf6e3;
  --white:#ffffff;
  --ink:#1b2a33;
  --accent:#ffa62b;
  --gap:#eef1f2;
}
*{box-sizing:border-box;margin:0;padding:0}
html,body{width:1200px;height:851px;overflow:hidden;background:var(--gap)}
body{position:relative;font-family:'Arimo',Arial,sans-serif;color:var(--white)}
.abs{position:absolute}

/* Screen frames */
.screen-frame{position:absolute;top:0;height:851px}
.menu-frame{left:0;width:579px;background:var(--menu-frame)}
.game-frame{left:621px;width:579px;background:var(--game-frame)}
.screen{position:absolute;background:var(--brand-teal)}
.menu-screen{left:27px;top:27px;width:525px;height:797px}
.game-screen{left:26px;top:27px;width:527px;height:795px}

/* Menu */
.app-title{left:0;width:514px;top:36px;text-align:center;font-size:35px;font-weight:700}
.outline-btn{top:92px;height:54px;border:2px solid var(--white);display:flex;align-items:center;justify-content:center;font-size:22.5px;letter-spacing:-.6px;white-space:nowrap}
.join-btn{left:15px;width:165px}
.create-btn{left:357px;width:165px}
.lobby-row{left:0;width:525px;height:50px;font-size:40px;line-height:50px;white-space:nowrap}
.lobby-row .player-count{position:absolute;left:64px}
.lobby-row .join-link{position:absolute;left:373px}
.select-box{left:11px;top:205px;width:38px;height:32px;background:var(--white)}
.select-box::after{content:"";position:absolute;left:9px;top:9px;width:20px;height:14px;background:var(--brand-teal)}
.play-band{left:0;top:577px;width:525px;height:79px;background:var(--paper);color:var(--ink);display:flex;align-items:center;justify-content:center;font-size:38px;font-weight:700}

/* Gameplay */
.timer-label{left:14px;top:42px;font-size:26px;font-weight:700;white-space:nowrap}
.timer-bar{left:224px;top:41px;width:262px;height:28px;background:var(--paper)}
.timer-fill{left:195px;top:6px;width:62px;height:17px;border:3px solid var(--brand-teal);background:var(--accent)}
.score-box{top:100px;width:69px;height:50px;background:var(--white)}
.score-box span{position:absolute;left:12px;right:12px;top:9px;bottom:11px;background:var(--brand-teal);display:flex;align-items:center;justify-content:center;font-size:25px}
.rank{left:443px;top:100px;font-size:31px;font-weight:700;white-space:nowrap}
.clue-panel{left:-3px;top:207px;width:528px;height:249px;background:var(--paper)}
.emoji-clue{left:164px;top:84px;width:120px;height:82px}
.answer-tile{width:56px;height:54px;background:var(--paper);border-radius:3px}
.letter-key{width:42px;height:58px;background:var(--white);border-radius:4px;color:var(--ink);font-size:27px;display:flex;align-items:center;justify-content:center}
</style>
</head>
<body>

<section class="screen-frame menu-frame" aria-label="Menu screen">
  <div class="screen menu-screen">
    <h1 class="abs app-title">Emoji Puzzles</h1>
    <div class="abs outline-btn join-btn">JOIN GAME</div>
    <div class="abs outline-btn create-btn">CREATE</div>

    <div class="abs select-box"></div>
    <div class="abs lobby-row" style="top:196px"><span class="player-count">3 Players</span><span class="join-link">JOIN &gt;</span></div>
    <div class="abs lobby-row" style="top:268px"><span class="player-count">3 Players</span><span class="join-link">JOIN &gt;</span></div>
    <div class="abs lobby-row" style="top:339px"><span class="player-count">3 Players</span><span class="join-link">JOIN &gt;</span></div>
    <div class="abs lobby-row" style="top:410px"><span class="player-count">3 Players</span><span class="join-link">JOIN &gt;</span></div>

    <div class="abs play-band">PLAY GAME</div>
  </div>
</section>

<section class="screen-frame game-frame" aria-label="Gameplay screen">
  <div class="screen game-screen">
    <div class="abs timer-label">60s Remaining</div>
    <div class="abs timer-bar"><div class="abs timer-fill"></div></div>

    <div class="abs score-box" style="left:15px"><span>4</span></div>
    <div class="abs score-box" style="left:96px"><span>4</span></div>
    <div class="abs score-box" style="left:177px"><span>3</span></div>
    <div class="abs score-box" style="left:258px"><span>2</span></div>
    <div class="abs score-box" style="left:339px"><span>2</span></div>
    <div class="abs rank">1 St.</div>

    <div class="abs clue-panel">
      <svg class="abs emoji-clue" viewBox="0 0 120 82" role="img" aria-label="Emoji clue: a pair of eyes">
        <defs>
          <linearGradient id="clueTone" x1="0" y1="0" x2="1" y2="1">
            <stop offset="0" stop-color="#d9d9d9"/>
            <stop offset="1" stop-color="#5a5a5a"/>
          </linearGradient>
        </defs>
        <rect x="0" y="0" width="120" height="82" rx="30" fill="url(#clueTone)"/>
      </svg>
    </div>

    <div class="abs answer-tile" style="left:95px;top:489px"></div>
    <div class="abs answer-tile" style="left:171px;top:489px"></div>
    <div class="abs answer-tile" style="left:247px;top:489px"></div>
    <div class="abs answer-tile" style="left:323px;top:489px"></div>
    <div class="abs answer-tile" style="left:399px;top:489px"></div>
    <div class="abs answer-tile" style="left:140px;top:555px"></div>
    <div class="abs answer-tile" style="left:216px;top:555px"></div>
    <div class="abs answer-tile" style="left:292px;top:555px"></div>
    <div class="abs answer-tile" style="left:368px;top:555px"></div>

    <div class="abs letter-key" style="left:42px;top:652px">E</div>
    <div class="abs letter-key" style="left:87px;top:652px">L</div>
    <div class="abs letter-key" style="left:133px;top:652px">P</div>
    <div class="abs letter-key" style="left:178px;top:652px">E</div>
    <div class="abs letter-key" style="left:224px;top:652px">G</div>
    <div class="abs letter-key" style="left:269px;top:652px">L</div>
    <div class="abs letter-key" style="left:315px;top:652px">P</div>
    <div class="abs letter-key" style="left:360px;top:652px">U</div>
    <div class="abs letter-key" style="left:406px;top:652px">Y</div>
    <div class="abs letter-key" style="left:451px;top:652px">K</div>

    <div class="abs letter-key" style="left:42px;top:716px">G</div>
    <div class="abs letter-key" style="left:87px;top:716px">P</div>
    <div class="abs letter-key" style="left:133px;top:716px">E</div>
    <div class="abs letter-key" style="left:178px;top:716px">S</div>
    <div class="abs letter-key" style="left:224px;top:716px">Y</div>
    <div class="abs letter-key" style="left:269px;top:716px">S</div>
    <div class="abs letter-key" style="left:315px;top:716px">E</div>
    <div class="abs letter-key" style="left:360px;top:716px">S</div>
    <div class="abs letter-key" style="left:406px;top:716px">P</div>
    <div class="abs letter-key" style="left:451px;top:716px">Y</div>
  </div>
</section>

</body>
</html>
```